A4 Client Referral Program Flyer for Property Management Agency

Harbourleaf Estates Agency is a property management specialist based on Sydney's Northern Beaches in Australia.

We manage mid to high-end rental properties for investors and property owners.
We are currently looking to build our portfolio and are offering existing clients and contacts a referral incentive. We want to sign up more properties to manage.

We are offering the referrer a $250 referral fee and the new owner 2 months of free management to entice them to use Harbourleaf Estates Agency.

We want an A4 Flyer to print and add to other document packages we hand out to clients and suppliers.
If at all possible a matching digital banner would be great too! 1000px wide x 250px

Please find copy attached in Word Doc and our logo attached also.

Please see our website for any more details on our business.

We must be able to have an editable photoshop version (PSD) of the document as well as a print ready PDF version incl any bleed necessary for A4 printing.

Target Market(s)

30-60YO Male and Female

Industry/Entity Type

Real Estate

Font styles to use
Sans Serif

Requirements
Must have
• Company Logo, contact details and copy provided

```html
<!DOCTYPE html>
<html lang="en">
<head>
<meta charset="utf-8">
<title>Harbourleaf Estates Agency – Referral Flyer</title>
<link href="https://fonts.googleapis.com/css2?family=Oswald:wght@500;600&family=Archivo+Black&family=Lato:wght@400;700&display=swap" rel="stylesheet">
<style>
  :root {
    --page-bg: #eceeef;
    --paper: #ffffff;
    --teal: #2a95a6;
    --teal-deep: #18788a;
    --teal-light: #45b6c3;
    --charcoal: #232323;
    --ink: #1d1d1d;
    --white: #ffffff;
  }
  * { box-sizing: border-box; margin: 0; padding: 0; }
  html, body { width: 900px; height: 1200px; overflow: hidden; }
  body { background: var(--page-bg); font-family: "Lato", Arial, sans-serif; color: var(--ink); }

  .flyer { position: absolute; left: 86px; top: 42px; width: 731px; height: 1023px; background: var(--paper); overflow: hidden; }

  .hero-photo { position: absolute; left: 0; top: 0; width: 731px; height: 385px;
    background: linear-gradient(180deg, #5fb6e0 0%, #a9d6ea 28%, #6d7f7a 52%, #3f6a3c 74%, #8a8f86 100%); }

  .brand { position: absolute; right: 26px; top: 60px; display: flex; align-items: center; gap: 8px;
    font-family: "Oswald", Arial, sans-serif; font-weight: 600; font-size: 22px; color: #1b1b1b; letter-spacing: 0.3px; }
  .brand-mark { width: 12px; height: 12px; background: var(--teal); }

  .decor { position: absolute; left: 0; top: 0; }

  .about { position: absolute; left: 22px; top: 465px; width: 355px; }
  .about-title { font-family: "Oswald", Arial, sans-serif; font-weight: 500; font-size: 18px; color: var(--teal-deep); margin-bottom: 4px; }
  .about-body { font-size: 10.8px; line-height: 14.4px; text-align: justify; }

  .referral-note { position: absolute; left: 22px; top: 678px; width: 355px; font-size: 10.8px; line-height: 14.4px; }
  .referral-note strong { font-family: "Oswald", Arial, sans-serif; font-size: 15px; }

  .url-bar { position: absolute; left: 0; top: 763px; width: 390px; height: 26px; background: var(--teal-deep);
    color: var(--white); font-family: "Oswald", Arial, sans-serif; font-weight: 500; font-size: 13.5px; line-height: 26px; padding-left: 22px; }

  .interior-photo { position: absolute; top: 814px; width: 132px; height: 90px; border: 3px solid var(--teal); }
  .interior-living { left: 38px; background: linear-gradient(135deg, #e8ecef 0%, #c9d4d6 50%, #9fb0a8 100%); }
  .interior-kitchen { left: 218px; background: linear-gradient(135deg, #f2f3f3 0%, #c8ced0 55%, #a9b98a 100%); }

  .offer { position: absolute; left: 390px; top: 490px; width: 341px; text-align: center; }
  .offer-invite { font-family: "Oswald", Arial, sans-serif; font-weight: 500; font-size: 37px; color: var(--white); line-height: 42px; letter-spacing: 0.3px; }
  .offer-receive { font-family: "Archivo Black", Arial, sans-serif; font-size: 29px; color: var(--teal-light); line-height: 36px; letter-spacing: 1px; }
  .offer-amount { font-family: "Oswald", Arial, sans-serif; font-weight: 600; font-size: 142px; color: var(--white); line-height: 148px; letter-spacing: -2px; }
  .offer-months { font-family: "Oswald", Arial, sans-serif; font-weight: 600; font-size: 27px; color: var(--teal-light); line-height: 32px; margin-top: 6px; }
  .offer-free { font-family: "Archivo Black", Arial, sans-serif; font-size: 18px; color: var(--white); line-height: 22px; letter-spacing: 0.5px; }

  .contacts { position: absolute; left: 410px; top: 792px; width: 310px; color: var(--white); font-size: 11.5px; }
  .contact { margin-bottom: 18px; }
  .contact-name { font-family: "Oswald", Arial, sans-serif; font-weight: 500; font-size: 13.5px; color: var(--teal-light); }
  .contact-role { font-family: "Lato", Arial, sans-serif; font-size: 11.5px; color: var(--white); }
  .contact-line { display: flex; align-items: center; gap: 7px; margin-top: 6px; }
  .contact-line svg { flex: none; }

  .footer-address { position: absolute; left: 24px; top: 946px; color: var(--white); font-size: 12px; line-height: 15px; }
  .footer-name { font-family: "Oswald", Arial, sans-serif; font-weight: 500; font-size: 13.5px; margin-bottom: 6px; }
  .footer-line { display: flex; align-items: flex-start; gap: 5px; }
  .footer-email { position: absolute; left: 268px; top: 978px; color: var(--white); font-size: 12px; display: flex; align-items: center; gap: 6px; }
</style>
</head>
<body>
<main class="flyer">
  <div class="hero-photo" role="img" aria-label="Photo of modern terraced townhouses with landscaped gardens and stairs under a blue sky"></div>
  <div class="brand"><span class="brand-mark"></span>HARBOURLEAF ESTATES</div>

  <svg class="decor" width="731" height="1023" viewBox="0 0 731 1023" aria-hidden="true">
    <polygon points="390,414 731,396 731,990 390,990" fill="var(--charcoal)"/>
    <polygon points="0,389 731,389 731,396 390,414 0,424" fill="var(--teal-deep)"/>
    <polygon points="0,390 731,390 731,393 0,393" fill="#9fdbe2"/>
    <polygon points="0,430 390,417 390,423 0,455" fill="var(--teal-light)"/>
    <polygon points="0,924 731,980 731,1023 0,1023" fill="var(--teal-deep)"/>
    <polygon points="0,924 731,976 731,981 0,929" fill="#bfe6eb"/>
  </svg>

  <section class="about">
    <h2 class="about-title">ABOUT US</h2>
    <p class="about-body">Harbourleaf Estates Agency is a full service agency specializing in property management on Sydney’s Northern Beaches.<br>
    We have a strong understanding of the local market, ensuring you get the best tenant, the best return and the highest quality of management and communication.<br>
    Property management is our core business and focus. You will get a professional, senior property manager looking after your property at all times.<br>
    We understand every owner/investor has different needs. Our aim is to personally tailor our services to satisfy those needs and ensure your experience with us is simple easy and confidence inspiring.</p>
  </section>

  <p class="referral-note"><strong>$250</strong> referral fee paid when the owner you refer signs their property for Management with Harbourleaf Estates Agency. Your referral must be submitted prior to signing on our website using the referral form on this page:</p>

  <div class="url-bar">http://www.harbourleafestates.com.au/referral-program/</div>

  <div class="interior-photo interior-living" role="img" aria-label="Photo of a bright living and dining room"></div>
  <div class="interior-photo interior-kitchen" role="img" aria-label="Photo of a white kitchen with bar stools"></div>

  <section class="offer">
    <p class="offer-invite">INVITE YOUR FRIENDS</p>
    <p class="offer-receive">AND RECEIVE</p>
    <p class="offer-amount">$250</p>
    <p class="offer-months">AND THEY GET 2 MONTHS</p>
    <p class="offer-free">FREE MANAGEMENT!</p>
  </section>

  <section class="contacts">
    <div class="contact">
      <p><span class="contact-name">Liam Carter –</span> <span class="contact-role">Director/Property Manager</span></p>
      <p class="contact-line"><svg width="9" height="9" viewBox="0 0 10 10"><path d="M2 0.5l2 2-1 1.3c.6 1.3 1.6 2.3 2.9 2.9L7.2 5.7l2 2-1.4 1.6C4.4 9 1 5.6.6 2z" fill="var(--teal-light)"/></svg>0412 555 018</p>
      <p class="contact-line"><svg width="9" height="9" viewBox="0 0 10 10"><rect x="0.5" y="2" width="9" height="6.5" rx="1" fill="var(--teal-light)"/></svg>liam@harbourleafestates.com.au</p>
    </div>
    <div class="contact">
      <p><span class="contact-name">Dario Voss –</span> <span class="contact-role">Built By Dario, Maintenance and Repairs</span></p>
      <p class="contact-line"><svg width="9" height="9" viewBox="0 0 10 10"><path d="M2 0.5l2 2-1 1.3c.6 1.3 1.6 2.3 2.9 2.9L7.2 5.7l2 2-1.4 1.6C4.4 9 1 5.6.6 2z" fill="var(--teal-light)"/></svg>0400 555 273</p>
      <p class="contact-line"><svg width="9" height="9" viewBox="0 0 10 10"><rect x="0.5" y="2" width="9" height="6.5" rx="1" fill="var(--teal-light)"/></svg>dario@builtbydario.com.au</p>
    </div>
  </section>

  <section class="footer-address">
    <p class="footer-name">Harbourleaf Estates Agency</p>
    <p class="footer-line"><svg width="8" height="11" viewBox="0 0 8 11"><path d="M4 0a4 4 0 0 1 4 4c0 3-4 7-4 7S0 7 0 4a4 4 0 0 1 4-4z" fill="var(--white)"/><circle cx="4" cy="4" r="1.4" fill="var(--teal-deep)"/></svg><span>PO Box 214<br>Dee Why, NSW 2099</span></p>
  </section>
  <p class="footer-email"><svg width="11" height="11" viewBox="0 0 10 10"><circle cx="5" cy="5" r="4.5" fill="none" stroke="var(--white)" stroke-width="1"/><path d="M0.5 5h9M5 .5c-2 2.5-2 6.5 0 9M5 .5c2 2.5 2 6.5 0 9" fill="none" stroke="var(--white)" stroke-width="0.8"/></svg>info@harbourleafestates.com.au</p>
</main>
</body>
</html>
```